Turm7Junior
Zielgruppe
Zielgruppe sind die Eltern, Lehrer, Kindergärtner, aber auch Kinder, die bereits Lesen können.
Aufgabenstellung
Ich brauche einen Flyer und ein Plakat für eine Kinderschachschule für Kinder zwischen 4 und 15 Jahren. Auf dem Flyer, den ich in A6-Format drucken möchte (beidseitig), muss ich die Info über die Kinderschachschule Turm7Junior (mehr Infos unter www.turm7junior-beispiel.ch), dh., was wir machen, Kontaktdaten, etc schreiben können. Es dient als Werbematerial zum Auslegen
Auf dem Plakat wird mehr oder weniger das Gleiche stehen, es wird jedoch als Din A4 Seite aufgehängt.
Unsere Kontaktinformation ist wie folgt:
Turm7Junior: Züge für kleine Denker
www.turm7junior-beispiel.ch

```html
<!DOCTYPE html>
<html lang="de">
<head>
<meta charset="utf-8">
<title>Turm7Junior – Plakat</title>
<link href="https://fonts.googleapis.com/css2?family=Mulish:ital,wght@0,400;0,600;0,800;1,600&display=swap" rel="stylesheet">
<style>
  :root {
    --bg: #e9e9e9;
    --paper: #ffffff;
    --ink: #1a1a1a;
    --magenta: #c2185b;
    --orange: #e8940f;
    --orange-light: #f6b949;
    --blue: #1e9ad6;
    --rule: #bdbdbd;
    --photo-warm-a: #b89a7a;
    --photo-warm-b: #d9c9b0;
    --photo-grey-a: #3a3a3a;
    --photo-grey-b: #a8a8a8;
    --board-faint: #ededed;
  }
  html, body {
    margin: 0;
    width: 1200px;
    height: 1200px;
    overflow: hidden;
    background: var(--bg);
    font-family: "Mulish", Arial, sans-serif;
    color: var(--ink);
  }
  .poster {
    position: absolute;
    left: 190px;
    top: 20px;
    width: 820px;
    height: 1160px;
    background: var(--paper);
    box-shadow: 0 4px 14px rgba(0,0,0,.12);
    overflow: hidden;
  }
  .brand {
    position: absolute;
    left: 40px;
    top: 38px;
    display: flex;
    align-items: center;
    gap: 10px;
  }
  .brand-square {
    width: 34px;
    height: 34px;
    background: var(--magenta);
  }
  .brand-name {
    font-weight: 800;
    font-size: 30px;
    color: var(--magenta);
    line-height: 1;
  }
  .brand-claim {
    position: absolute;
    left: 40px;
    top: 84px;
    font-size: 13px;
    font-weight: 600;
    color: var(--ink);
  }
  .tagline-band {
    position: absolute;
    left: 270px;
    right: 0;
    top: 58px;
    height: 34px;
    background: linear-gradient(180deg, var(--orange-light), var(--orange));
    color: #fff;
    font-style: italic;
    font-weight: 600;
    font-size: 18px;
    line-height: 34px;
    padding-left: 30px;
  }
  .header-rule {
    position: absolute;
    left: 40px;
    right: 0;
    top: 118px;
    height: 3px;
    background: var(--rule);
  }
  .why-title {
    position: absolute;
    left: 44px;
    top: 196px;
    margin: 0;
    font-size: 28px;
    font-weight: 800;
    color: var(--magenta);
    white-space: nowrap;
  }
  .why-list {
    position: absolute;
    left: 56px;
    top: 284px;
    margin: 0;
    padding: 0;
    list-style: none;
    font-size: 24px;
    font-weight: 800;
  }
  .why-list li { margin-bottom: 40px; }
  .photo-tournament {
    position: absolute;
    left: 420px;
    top: 175px;
    width: 372px;
    height: 300px;
    background: linear-gradient(135deg, var(--photo-warm-a), var(--photo-warm-b));
  }
  .quote {
    position: absolute;
    left: 0;
    right: 0;
    top: 510px;
    text-align: center;
    margin: 0;
  }
  .quote-text {
    font-size: 30px;
    font-weight: 800;
    color: var(--orange);
    display: block;
  }
  .quote-source {
    font-size: 18px;
    display: block;
    margin-top: 2px;
  }
  .offer-title {
    position: absolute;
    right: 44px;
    top: 612px;
    margin: 0;
    font-size: 28px;
    font-weight: 800;
    color: var(--blue);
  }
  .photo-child {
    position: absolute;
    left: 44px;
    top: 680px;
    width: 360px;
    height: 320px;
    background: linear-gradient(160deg, var(--photo-grey-b), var(--photo-grey-a));
  }
  .offer-list {
    position: absolute;
    right: 44px;
    top: 702px;
    margin: 0;
    padding: 0;
    list-style: none;
    text-align: right;
    font-size: 21px;
    font-weight: 800;
  }
  .offer-list li { margin-bottom: 22px; }
  .board-decor {
    position: absolute;
    left: 0;
    right: 0;
    bottom: 0;
    height: 220px;
    background: linear-gradient(180deg, rgba(237,237,237,0), var(--board-faint));
  }
  .contact {
    position: absolute;
    left: 0;
    right: 0;
    top: 1012px;
    text-align: center;
    font-size: 21px;
    line-height: 36px;
  }
  .contact span { margin: 0 10px; }
  .web-cta {
    position: absolute;
    left: 0;
    right: 0;
    top: 1100px;
    text-align: center;
    font-size: 21px;
    font-weight: 800;
  }
  .web-cta .url { color: var(--magenta); }
</style>
</head>
<body>
  <main class="poster">
    <div class="brand">
      <div class="brand-square"></div>
      <div class="brand-name">Turm7Junior</div>
    </div>
    <div class="brand-claim">Züge für kleine Denker</div>
    <div class="tagline-band">Wir bringen Ihr Kind Zug um Zug zum Erfolg</div>
    <div class="header-rule"></div>

    <h2 class="why-title">Warum Kinderschach?</h2>
    <ul class="why-list">
      <li>Schach macht schlau.</li>
      <li>Schach macht stark.</li>
      <li>Schach macht Spass.</li>
    </ul>
    <div class="photo-tournament" role="img" aria-label="Foto: Kinder spielen an langen Tischen Schach in einem Turnier"></div>

    <p class="quote">
      <span class="quote-text">“Schach ist die spielerische Antwort auf Pisa.“</span>
      <span class="quote-source">Konrad Albrecht, Präsident des Landesschachverbands Nord</span>
    </p>

    <div class="board-decor" role="img" aria-label="Dezentes Schachbrettmuster im Hintergrund"></div>

    <h2 class="offer-title">Wir bieten Ihrem Kind:</h2>
    <div class="photo-child" role="img" aria-label="Schwarzweissfoto: Junge zählt nachdenklich an den Fingern"></div>
    <ul class="offer-list">
      <li>Konzentrationstraining</li>
      <li>Intellektuelle Förderung</li>
      <li>Stärkung des Selbstvertrauens</li>
      <li>Persönliches Wachstum</li>
      <li>Spass und Spannung</li>
    </ul>

    <div class="contact">
      <div><span>Turm7Junior</span><span>Postfach 410</span><span>Tel. 079 000 12 34</span></div>
      <div><span>Lindenweg 12</span><span>8700 Musterdorf</span><span>info@turm7junior-beispiel.ch</span></div>
    </div>
    <div class="web-cta">Mehr Infos im Internet auf <span class="url">www.turm7junior-beispiel.ch</span></div>
  </main>
</body>
</html>
```